r-brightlayer needs new website

need to get completely new updated site for r-brightlayer.com
general business concepts can be started from that site and I can offer specifick input about business operations and goals. would like to offer on-line ordering, service requests, and payments if possible.

```html
<!DOCTYPE html>
<html lang="en">
<head>
<meta charset="utf-8">
<title>Corvalin International</title>
<link rel="stylesheet" href="https://fonts.googleapis.com/css2?family=Open+Sans:wght@400;700&family=Raleway:wght@300;400;600;700&display=swap">
<style>
:root{
  --red:#e3141e;
  --red-dark:#a5060c;
  --ink:#1b1b1b;
  --text:#333;
  --soft:#f7f5f5;
  --tile:#efefef;
  --night:#000;
  --white:#fff;
}
*{margin:0;padding:0;box-sizing:border-box}
html,body{width:1200px;height:3364px;overflow:hidden}
body{position:relative;background:var(--white);font-family:"Raleway",sans-serif;color:var(--text)}
.abs{position:absolute}
.btn{position:absolute;display:flex;align-items:center;justify-content:center;font-family:"Open Sans",sans-serif;font-weight:700;font-size:18px;text-transform:uppercase;letter-spacing:.3px}
.btn-outline{border:3px solid var(--red);color:var(--red);background:var(--white)}
.btn-solid{background:var(--red);color:var(--white)}

/* header + hero */
.hero{left:0;top:0;width:1200px;height:635px;background:var(--soft)}
.brand{left:94px;top:22px;display:flex;align-items:center;gap:10px;font-weight:700;font-size:18px;color:var(--ink);white-space:nowrap}
.brand-dot{width:30px;height:30px;border-radius:50%;background:var(--red)}
.nav{top:30px;font-family:"Open Sans",sans-serif;font-size:12px;font-weight:700;color:var(--ink);white-space:nowrap}
.hero-title{left:92px;top:208px;font-weight:700;font-size:48px;line-height:54px;color:var(--ink)}
.hero-title .accent{display:block;color:var(--red);font-size:72px;line-height:80px}
.hero-photo{left:621px;top:126px;width:438px;height:397px;background:radial-gradient(circle at 65% 40%,#3a3a3a 0 28%,transparent 29%),linear-gradient(135deg,#f02a30,var(--red-dark))}
.hero-frame{left:763px;top:220px;width:385px;height:352px;border:10px solid var(--red);border-top:none;border-left:none}
.hero-frame::before{content:"";position:absolute;left:0;bottom:0;width:10px;height:60px;background:var(--red)}
.hero-frame::after{content:"";position:absolute;top:0;right:-10px;width:60px;height:10px;background:var(--red)}

/* about */
.about-photo{left:94px;top:790px;width:424px;height:358px;background:linear-gradient(135deg,#f4ece6,#d9b899 60%,#b98a62)}
.about-frame{left:22px;top:866px;width:388px;height:356px;border:12px solid var(--red);border-top:none;border-right:none}
.about-frame::before{content:"";position:absolute;left:-12px;top:0;width:72px;height:12px;background:var(--red)}
.about-frame::after{content:"";position:absolute;right:0;top:280px;width:12px;height:76px;background:var(--red)}
.about-title{right:94px;top:715px;font-weight:700;font-size:64px;color:var(--ink)}
.about-sub{right:94px;top:850px;font-weight:400;font-size:34px;color:var(--ink)}
.about-copy{right:94px;top:910px;width:540px;text-align:right;font-size:13px;line-height:20px;color:var(--text)}
.about-copy p+p{margin-top:18px}

/* mission */
.mission{left:0;top:1312px;width:1200px;height:422px;background:radial-gradient(ellipse at 75% 60%,#4a4a4a,transparent 55%),radial-gradient(ellipse at 20% 50%,#3c3c3c,transparent 50%),#232323;color:var(--white);text-align:center}
.mission-title{top:64px;width:100%;font-weight:600;font-size:62px}
.mission-sub{top:166px;width:100%;font-weight:600;font-size:34px}
.mission-copy{top:224px;left:130px;width:940px;font-size:12px;line-height:19px}
.mission-copy p+p{margin-top:10px}

/* applications */
.apps-title{top:1822px;width:100%;text-align:center;font-weight:600;font-size:66px;color:var(--ink)}
.apps-grid{left:94px;top:1954px;width:1012px;height:670px;display:grid;grid-template-columns:repeat(3,1fr);grid-template-rows:repeat(2,1fr)}
.tile-photo{background:radial-gradient(ellipse at 55% 50%,#e9e9e9 0 22%,transparent 38%),radial-gradient(circle at 50% 50%,#ff4a4f,var(--red-dark) 80%)}
.tile-app{background:var(--tile);display:flex;flex-direction:column;align-items:center;justify-content:center;text-align:center;font-weight:700;font-size:30px;line-height:32px;color:#3d3d3d}
.tile-app svg{margin-bottom:10px}

/* footer */
.footer{left:0;top:2793px;width:1200px;height:571px;background:var(--night);color:var(--white)}
.thanks{left:94px;top:80px;font-family:"Open Sans",sans-serif;font-size:11px;line-height:17px;text-transform:uppercase}
.field{left:94px;width:449px;border:1px solid #bbb;font-family:"Open Sans",sans-serif;font-size:10px;color:#bbb;padding:8px 10px}
.submit{left:94px;top:412px;width:67px;height:23px;font-size:10px}
.contact-title{left:624px;top:94px;font-family:"Open Sans",sans-serif;font-weight:700;font-size:17px;text-transform:uppercase}
.contact-item{left:624px;display:flex;gap:18px;font-family:"Open Sans",sans-serif;font-size:10px;line-height:17px}
.contact-item svg{flex:none;margin-top:2px}
.map{left:890px;top:152px;width:216px;height:175px;background:linear-gradient(135deg,#f1ede6,#e3ddd3)}
.copyright{top:490px;width:100%;text-align:center;font-family:"Open Sans",sans-serif;font-weight:700;font-size:10px}
</style>
</head>
<body>

<section class="abs hero">
  <div class="abs brand"><span class="brand-dot"></span>Corvalin International</div>
  <span class="abs nav" style="left:518px">HOME</span>
  <span class="abs nav" style="left:585px">ABOUT US</span>
  <span class="abs nav" style="left:673px">OUR MISSION</span>
  <span class="abs nav" style="left:778px">APPLICATIONS</span>
  <span class="abs nav" style="left:886px">CONTACT</span>
  <a class="btn btn-solid" style="left:973px;top:13px;width:133px;height:45px">Buy Now</a>

  <h1 class="abs hero-title">Imaging<br>Solutions For<span class="accent">Your Business</span></h1>
  <a class="btn btn-outline" style="left:94px;top:437px;width:164px;height:52px">Learn More</a>

  <div class="abs hero-frame"></div>
  <div class="abs hero-photo" role="img" aria-label="Desktop check scanner printer on a red background"></div>
</section>

<section>
  <div class="abs about-frame"></div>
  <div class="abs about-photo" role="img" aria-label="Hands passing a payment card across a desk beside a tablet"></div>
  <h2 class="abs about-title">About Us</h2>
  <h3 class="abs about-sub">We Provide Valuable Solutions</h3>
  <div class="abs about-copy">
    <p>Corvalin is an Imaging Solutions company based out of Central Illinois. Being from a small town, we keep our roots in honesty and hospitality, yet our product solutions are on the cutting edge of technology.</p>
    <p>We not only provide our customers valuable solutions, we do it well. We understand the needs of the institutions we serve and have the means to stay up to date on the latest advancements in the industry. From simple check archive to complex corporate payment processing systems and everything in between, we have complete solutions that are cost effective and user friendly.</p>
  </div>
  <a class="btn btn-outline" style="left:942px;top:1124px;width:164px;height:54px">Learn More</a>
</section>

<section class="abs mission" role="img" aria-label="Dimmed photo of business people at work behind the mission text">
  <h2 class="abs mission-title">Our Mission</h2>
  <h3 class="abs mission-sub">How We Do Business</h3>
  <div class="abs mission-copy">
    <p>CORVALIN strives to be the leading provider of cost-effective software, hardware, and turnkey solutions to the Business, Utility, and Banking Marketplace.</p>
    <p>We know that technology is extremely important in giving our customers a competitive advantage. We also realize that the need to keep up with technology is not in the everyday realm of many business owners expertise so we can offer significant value in providing complete solutions with ongoing support.</p>
    <p>We also believe that the solution should fit your operation instead of disrupting or rebuilding it and be so simple to install and learn that you wonder why you haven't had it forever.</p>
  </div>
</section>

<section>
  <h2 class="abs apps-title">Applications</h2>
  <div class="abs apps-grid">
    <div class="tile-photo" role="img" aria-label="Check scanner on a red background"></div>
    <div class="tile-app">
      <svg width="38" height="44" viewBox="0 0 38 44" fill="none" stroke="#e3141e" stroke-width="4"><circle cx="7" cy="7" r="5"/><circle cx="31" cy="7" r="5"/><circle cx="19" cy="37" r="5"/><path d="M7 12v6c0 6 12 6 12 12M31 12v6c0 6-12 6-12 12"/></svg>
      Branch<br>Transformation</div>
    <div class="tile-photo" role="img" aria-label="Check scanner on a red background"></div>
    <div class="tile-app">
      <svg width="38" height="44" viewBox="0 0 38 44" fill="none" stroke="#e3141e" stroke-width="4"><circle cx="7" cy="7" r="5"/><circle cx="31" cy="7" r="5"/><circle cx="19" cy="37" r="5"/><path d="M7 12v6c0 6 12 6 12 12M31 12v6c0 6-12 6-12 12"/></svg>
      Branch<br>Transformation</div>
    <div class="tile-photo" role="img" aria-label="Check scanner on a red background"></div>
    <div class="tile-app">
      <svg width="38" height="44" viewBox="0 0 38 44" fill="none" stroke="#e3141e" stroke-width="4"><circle cx="7" cy="7" r="5"/><circle cx="31" cy="7" r="5"/><circle cx="19" cy="37" r="5"/><path d="M7 12v6c0 6 12 6 12 12M31 12v6c0 6-12 6-12 12"/></svg>
      Branch<br>Transformation</div>
  </div>
  <a class="btn btn-outline" style="left:516px;top:2671px;width:164px;height:54px">See More</a>
</section>

<footer class="abs footer">
  <p class="abs thanks">Thanks for visiting our site.<br>We look forward to serving your technology needs whether large or small.</p>
  <div class="abs field" style="top:152px;height:32px">Name</div>
  <div class="abs field" style="top:192px;height:32px">Subject</div>
  <div class="abs field" style="top:231px;height:32px">Email</div>
  <div class="abs field" style="top:271px;height:121px">Message</div>
  <a class="btn btn-solid submit">Submit</a>

  <h3 class="abs contact-title">Contact</h3>
  <div class="abs contact-item" style="top:150px">
    <svg width="10" height="14" viewBox="0 0 10 14"><path d="M5 0a5 5 0 0 1 5 5c0 4-5 9-5 9S0 9 0 5a5 5 0 0 1 5-5z" fill="#e3141e"/><circle cx="5" cy="5" r="2" fill="#000"/></svg>
    <span>420 North Elm Avenue<br>Maple Grove, IL 60000</span></div>
  <div class="abs contact-item" style="top:198px">
    <svg width="10" height="14" viewBox="0 0 10 14"><rect x="1" y="0" width="8" height="14" rx="2" fill="#e3141e"/><rect x="3" y="2" width="4" height="8" fill="#000"/></svg>
    <span>Telephone: 555-014-2271</span></div>
  <div class="abs contact-item" style="top:234px">
    <svg width="12" height="12" viewBox="0 0 12 12"><rect x="0" y="3" width="12" height="7" rx="1" fill="#e3141e"/><rect x="3" y="0" width="6" height="4" fill="#e3141e"/></svg>
    <span>Fax: 555-014-2290</span></div>
  <div class="abs contact-item" style="top:268px">
    <svg width="12" height="10" viewBox="0 0 12 10"><rect width="12" height="10" rx="1" fill="#e3141e"/><path d="M0 1l6 5 6-5" stroke="#000" fill="none"/></svg>
    <span>General Information:<br>info@r-brightlayer.com<br>Sales<br>sales@r-brightlayer.com<br>Customer Support<br>support@r-brightlayer.com Webmaster<br>webmaster@r-brightlayer.com</span></div>
  <div class="abs map" role="img" aria-label="Street map showing the office location"></div>

  <p class="abs copyright">© 2019 R-BRIGHTLAYER.COM. ALL RIGHTS RESERVED.</p>
</footer>

</body>
</html>
```